Very Simple/Minimal Business Card Design Project

The company operates in the industrial maritime infrastructure sector in Brazil. You can find more information on our website www.navelquor.com.br WE NEED TO LOOK POWERFUL AND SERIOUS
I have attached a copy of the old cards. We would like something more professional / industrial / sexy that also includes the position.

The card can be double sided or not. We would like you to propose as many options.

Thank you
Updates

Many thanks, do let me know if you have any questions. I am under a lot of time pressure to try and have them printed over the next days or so.

Please could you use the following information

for the address: Rua Tapiraçu, 418 - Centro, Rio de Janeiro, 20135-070, Brasil

for the mobile: +55 21 8372 9041
for the landline: +55 21 4067 3859

and position:  Diretor Geral

Thakn you

Target Market(s)

Shipowners, bankers, industrial companies

Industry/Entity Type

Industrial

Requirements
Must have
• POWERFUL
SERIOUS
SOLID
BIG CORPORATION

```html
<!DOCTYPE html>
<html lang="pt-BR">
<head>
<meta charset="utf-8">
<title>Navelquor – Cartão de Visita</title>
<link rel="stylesheet" href="https://fonts.googleapis.com/css2?family=Open+Sans:wght@600;700;800&display=swap">
<style>
  :root {
    --brand-green: #66b32e;
    --brand-navy: #27357e;
    --band-white: #f4f4f3;
    --card-edge: #141414;
    --page-bg: #e9e7e3;
    --text-light: #ffffff;
  }
  * { box-sizing: border-box; margin: 0; padding: 0; }
  html, body {
    width: 1200px; height: 900px; overflow: hidden;
    background: var(--page-bg);
    font-family: "Open Sans", Arial, sans-serif;
  }
  .card {
    position: absolute;
    border: 8px solid var(--card-edge);
    border-radius: 24px;
    overflow: hidden;
    background: var(--brand-green);
  }
  .card--front { left: 110px; top: 40px; width: 618px; height: 382px; }
  .card--back  { left: 393px; top: 470px; width: 612px; height: 382px; }

  .brand-band {
    position: absolute; left: 0; right: 0;
    background: var(--band-white);
    display: flex; align-items: center;
  }
  .card--front .brand-band { top: 122px; height: 124px; padding-left: 129px; }
  .card--back .brand-band  { top: 0; height: 119px; padding-left: 115px; }

  .brand { display: flex; align-items: center; gap: 10px; }
  .brand__mark {
    width: 70px; height: 72px; border-radius: 8px;
    background: var(--brand-green);
  }
  .brand__name {
    font-weight: 800; font-size: 40px; letter-spacing: 0.5px;
    color: var(--brand-navy); line-height: 1;
  }

  .holder {
    position: absolute; top: 170px; left: 0; right: 0;
    text-align: center; color: var(--text-light);
  }
  .holder__name { font-weight: 700; font-size: 35px; line-height: 44px; }
  .holder__role { font-weight: 600; font-size: 17px; line-height: 22px; }

  .contact {
    position: absolute; color: var(--text-light);
    font-weight: 700; font-size: 15.5px; line-height: 21.5px;
    list-style: none;
  }
  .contact--phone   { left: 18px; top: 264px; }
  .contact--address { left: 415px; top: 259px; }
</style>
</head>
<body>
  <section class="card card--front" aria-label="Frente do cartão">
    <div class="brand-band">
      <div class="brand">
        <span class="brand__mark"></span>
        <span class="brand__name">NAVELQUOR</span>
      </div>
    </div>
  </section>

  <section class="card card--back" aria-label="Verso do cartão">
    <div class="brand-band">
      <div class="brand">
        <span class="brand__mark"></span>
        <span class="brand__name">NAVELQUOR</span>
      </div>
    </div>
    <div class="holder">
      <h1 class="holder__name">Rafael Moreau</h1>
      <p class="holder__role">Diretor Geral</p>
    </div>
    <ul class="contact contact--phone">
      <li>T: + 55 21 4067 3859</li>
      <li>M: + 55 21 8372 9041</li>
      <li>rafael@navelquor.com.br</li>
      <li>www.navelquor.com.br</li>
    </ul>
    <ul class="contact contact--address">
      <li>Rua Tapiraçu, 418</li>
      <li>Centro</li>
      <li>CEP 20135-070</li>
      <li>Rio de Janeiro</li>
    </ul>
  </section>
</body>
</html>
```